Healthcare technology company needs website design

We need a logo for a new company based in the U.S. We develop software to assist consumers identifying lowest cost healthcare coverage methods, including insurance, discount cards, and cash options. We would like to see designs that use multiple shades of green with the optional addition of other complimentary colors. The final design should communicate a unique blend of saving money while receiving the healthcare you need.
Need the following pages/sections: Homepage, Solutions, About Us, Contact
Competitors: www.velorinhealth.example; www.qdplm.example

Target Market(s)

Businesses

Industry/Entity Type

Healthcare

Coding

Coded - Design and coding required

Number of Pages Required

4 page

Colors
0054AA
0677BA
7BADD7
CADEEF
E8F1F8
00AB8E
00BBA5
67D7C9
C6EFE9
E9F9F6

Requirements
Must have
• Matching color theme with logo
Nice to have
• Animated background

```html
<!DOCTYPE html>
<html lang="en">
<head>
<meta charset="utf-8">
<title>Verdance Health</title>
<link href="https://fonts.googleapis.com/css2?family=Montserrat:wght@400;500;600;700&display=swap" rel="stylesheet">
<style>
:root{
  --blue-deep:#0054AA;
  --blue:#0677BA;
  --blue-soft:#7BADD7;
  --blue-pale:#CADEEF;
  --blue-mist:#E8F1F8;
  --green:#00AB8E;
  --green-mid:#00BBA5;
  --green-soft:#67D7C9;
  --green-pale:#C6EFE9;
  --green-mist:#E9F9F6;
  --ink:#111111;
  --white:#ffffff;
}
*{margin:0;padding:0;box-sizing:border-box}
html,body{width:1200px;height:4795px;overflow:hidden;background:var(--white)}
body{position:relative;font-family:'Montserrat',sans-serif;color:var(--ink)}
.abs{position:absolute}
.center{left:0;width:1200px;text-align:center}

/* hero */
.hero{left:0;top:0;width:1200px;height:599px;background:linear-gradient(120deg,#f4f5f7 0%,#e9ebef 55%,#dde1e8 100%)}
.brand{left:43px;top:42px;display:flex;align-items:center;gap:16px}
.brand-dot{width:72px;height:72px;border-radius:50%;background:var(--green)}
.brand-name{font-weight:700;font-size:40px;letter-spacing:2px;color:var(--green)}
.nav{top:32px;font-weight:700;font-size:20px;letter-spacing:.3px;color:var(--ink)}
.hero-accent{left:52px;top:408px;width:11px;height:171px;background:var(--green-soft)}
.hero-title{left:99px;top:402px;font-weight:500;font-size:52px;line-height:58px;letter-spacing:3px;color:var(--ink)}

/* headings */
.section-title{font-weight:500;font-size:50px;letter-spacing:4px;line-height:1;color:var(--ink)}
.lead{font-weight:400;font-size:31px;line-height:36px;letter-spacing:1.5px;color:var(--blue-soft)}
.lead.on-color{color:var(--white)}

/* mission / vision */
.pillar-title{font-weight:500;font-size:52px;letter-spacing:3px;line-height:1}
.pillar-text{font-size:31px;letter-spacing:1.5px;color:var(--blue-soft);line-height:1}

/* problem band */
.problem{left:0;top:1163px;width:1200px;height:598px;background:linear-gradient(180deg,#06739f 0%,#0a7db0 55%,#0a86b8 100%)}
.problem-hand{left:360px;top:1230px;width:520px;height:531px;border-radius:200px 200px 40px 40px;background:radial-gradient(ellipse at 50% 45%,rgba(40,110,210,.85),rgba(10,90,180,.25) 70%,rgba(10,90,180,0) 100%)}
.tag{left:1074px;top:1185px}
.band-title{font-weight:500;font-size:52px;letter-spacing:4px;line-height:1;color:var(--white)}

/* solution bands */
.solution{left:0;width:1200px;height:598px;background:linear-gradient(90deg,var(--green) 0%,var(--green-mid) 40%,var(--green-soft) 100%)}

/* people */
.avatar{width:302px;height:302px}
.role{font-weight:500;font-size:50px;letter-spacing:4px;line-height:1}
.detail{font-size:31px;letter-spacing:1.5px;color:var(--blue-soft);line-height:1}

/* footer */
.footer-line{left:0;top:4461px;width:1200px;height:17px;background:var(--blue)}
.footer-brand{left:70px;top:4580px;font-weight:700;font-size:26px;letter-spacing:1px;color:var(--green)}
.footer-divider{left:250px;top:4489px;width:2px;height:216px;background:var(--blue-pale)}
.foot-item{font-size:19px;letter-spacing:.5px;color:var(--blue);line-height:1;display:flex;align-items:center}
.copyright{left:0;top:4727px;width:1200px;height:68px;background:var(--blue);color:var(--white);font-size:19px;letter-spacing:.5px;display:flex;align-items:center;justify-content:center}
</style>
</head>
<body>

<!-- hero -->
<div class="abs hero" role="img" aria-label="Photo of two hands gently holding each other on a soft grey background"></div>
<div class="abs brand"><span class="brand-dot"></span><span class="brand-name">VERDANCE HEALTH</span></div>
<div class="abs nav" style="left:707px">SOLUTION</div>
<div class="abs nav" style="left:874px">ABOUT US</div>
<div class="abs nav" style="left:1038px">CONTACT</div>
<div class="abs hero-accent"></div>
<h1 class="abs hero-title">Guide You to<br>True Future<br>Healtcare</h1>

<!-- profile -->
<h2 class="abs center section-title" style="top:686px">OUR PROFILE</h2>
<p class="abs center lead" style="top:764px">We are healthcare technology<br>services company that’s guide you<br>to get new True Future Healthcare</p>

<svg class="abs" style="left:127px;top:972px" width="94" height="104" viewBox="0 0 94 104" fill="none" stroke="#00BBA5" stroke-width="6" stroke-linecap="round" stroke-linejoin="round">
  <path d="M47 22c-15 0-25 11-25 24 0 9 5 15 10 20 3 3 4 7 4 11v6h22v-6c0-4 1-8 4-11 5-5 10-11 10-20 0-13-10-24-25-24z"/>
  <path d="M36 90h22M40 99h14"/>
  <path d="M47 3v8M16 14l6 6M78 14l-6 6M4 44h8M82 44h8M10 72l7-4M84 72l-7-4"/>
</svg>
<div class="abs pillar-title" style="left:246px;top:983px">Mission</div>
<div class="abs pillar-text" style="left:246px;top:1044px">Our mission is..</div>

<svg class="abs" style="left:726px;top:975px" width="80" height="100" viewBox="0 0 80 100" fill="none" stroke="#00BBA5" stroke-width="6" stroke-linejoin="round">
  <circle cx="40" cy="33" r="28"/>
  <path d="M40 20l4 9 10 1-7 7 2 10-9-5-9 5 2-10-7-7 10-1z" fill="#00BBA5" stroke-width="2"/>
  <path d="M24 56L12 92l14-6 8 12 6-20M56 56l12 36-14-6-8 12-6-20"/>
</svg>
<div class="abs pillar-title" style="left:843px;top:983px">Vision</div>
<div class="abs pillar-text" style="left:843px;top:1044px">To become a..</div>

<!-- problem -->
<div class="abs problem" role="img" aria-label="Photo of a translucent blue robotic hand held up, palm forward"></div>
<div class="abs problem-hand" aria-hidden="true"></div>
<svg class="abs tag" width="100" height="71" viewBox="0 0 100 71"><path d="M0 35.5L36 0H100V71H36Z" fill="#7BADD7" opacity=".85"/></svg>
<h2 class="abs center band-title" style="top:1623px">BIGGEST PUBLIC PROBLEM</h2>
<p class="abs center lead" style="top:1783px">We are identifying lowest cost healthcare<br>coverage methods, including insurance,<br>discount cards, and cash options</p>

<!-- solution one -->
<section class="abs solution" style="top:2028px"></section>
<svg class="abs" style="left:537px;top:2088px" width="110" height="145" viewBox="0 0 110 145" fill="none" stroke="#fff" stroke-width="9" stroke-linejoin="round">
  <path d="M70 5L8 82h44l-12 58 62-80H58z"/>
</svg>
<h2 class="abs center band-title" style="top:2311px;font-size:50px">OUR SOLUTION</h2>
<p class="abs center lead on-color" style="top:2392px">We are identifying lowest cost healthcare<br>coverage methods, including insurance,<br>discount cards, and cash options</p>

<!-- solution two -->
<section class="abs solution" style="top:2663px"></section>
<svg class="abs" style="left:527px;top:2730px" width="146" height="145" viewBox="0 0 146 145" fill="none" stroke="#fff" stroke-width="9" stroke-linejoin="round" stroke-linecap="round">
  <path d="M6 2v138h136"/>
  <path d="M26 140V95M52 140V80M78 140V100M104 140V85M128 140V70"/>
  <path d="M20 70l30-25 28 22 44-40"/>
  <path d="M104 24h20v20"/>
</svg>
<h2 class="abs center band-title" style="top:2945px;font-size:50px">OUR SOLUTION</h2>
<p class="abs center lead on-color" style="top:3027px">We are identifying lowest cost healthcare<br>coverage methods, including insurance,<br>discount cards, and cash options</p>

<!-- people -->
<svg width="0" height="0" style="position:absolute">
  <defs>
    <linearGradient id="avatarFill" x1="0" y1="0" x2="1" y2="1">
      <stop offset="0" stop-color="#7BADD7"/><stop offset="1" stop-color="#0054AA"/>
    </linearGradient>
    <symbol id="avatar" viewBox="0 0 302 302">
      <circle cx="151" cy="151" r="151" fill="url(#avatarFill)"/>
      <circle cx="151" cy="151" r="90" fill="none" stroke="#fff" stroke-width="16"/>
      <circle cx="151" cy="126" r="28" fill="#fff"/>
      <path d="M96 214c10-30 32-46 55-46s45 16 55 46" fill="#fff"/>
    </symbol>
  </defs>
</svg>
<svg class="abs avatar" style="left:447px;top:3392px"><use href="#avatar"/></svg>
<h3 class="abs center role" style="top:3744px">FOUNDER</h3>
<div class="abs center detail" style="top:3813px">Detail Profile</div>

<svg class="abs avatar" style="left:149px;top:3928px"><use href="#avatar"/></svg>
<h3 class="abs role" style="left:0;width:600px;text-align:center;top:4279px">TEAM</h3>
<div class="abs detail" style="left:0;width:600px;text-align:center;top:4349px">Detail Profile</div>

<svg class="abs avatar" style="left:748px;top:3928px"><use href="#avatar"/></svg>
<h3 class="abs role" style="left:600px;width:600px;text-align:center;top:4279px">TEAM</h3>
<div class="abs detail" style="left:600px;width:600px;text-align:center;top:4349px">Detail Profile</div>

<!-- footer -->
<footer>
  <div class="abs footer-line"></div>
  <div class="abs footer-brand">VERDANCE</div>
  <div class="abs footer-divider"></div>

  <svg class="abs" style="left:290px;top:4495px" width="22" height="22" viewBox="0 0 24 24" fill="none" stroke="#7BADD7" stroke-width="1.8" stroke-linejoin="round"><path d="M5 3h4l2 5-3 2a11 11 0 0 0 6 6l2-3 5 2v4a2 2 0 0 1-2 2A18 18 0 0 1 3 5a2 2 0 0 1 2-2z"/></svg>
  <div class="abs foot-item" style="left:350px;top:4497px">Phone Number</div>
  <svg class="abs" style="left:290px;top:4558px" width="22" height="22" viewBox="0 0 24 24" fill="none" stroke="#7BADD7" stroke-width="1.8"><rect x="2" y="5" width="20" height="14" rx="1"/><path d="M2 6l10 7 10-7"/></svg>
  <div class="abs foot-item" style="left:350px;top:4558px">Email Address</div>
  <svg class="abs" style="left:290px;top:4622px" width="24" height="24" viewBox="0 0 24 24" fill="none" stroke="#7BADD7" stroke-width="1.8"><rect x="6" y="2" width="12" height="6"/><rect x="3" y="8" width="18" height="9" rx="1"/><rect x="6" y="14" width="12" height="8"/></svg>
  <div class="abs foot-item" style="left:350px;top:4623px">Fax</div>

  <svg class="abs" style="left:664px;top:4496px" width="28" height="20" viewBox="0 0 28 20"><path d="M0 10L10 0H28V20H10Z" fill="#67D7C9"/></svg>
  <div class="abs foot-item" style="left:707px;top:4497px">Solutions</div>
  <svg class="abs" style="left:664px;top:4557px" width="28" height="20" viewBox="0 0 28 20"><path d="M0 10L10 0H28V20H10Z" fill="#67D7C9"/></svg>
  <div class="abs foot-item" style="left:707px;top:4558px">About Us</div>
  <svg class="abs" style="left:664px;top:4622px" width="28" height="20" viewBox="0 0 28 20"><path d="M0 10L10 0H28V20H10Z" fill="#67D7C9"/></svg>
  <div class="abs foot-item" style="left:707px;top:4623px">Contact</div>

  <svg class="abs" style="left:923px;top:4496px" width="28" height="20" viewBox="0 0 28 20"><path d="M0 10L10 0H28V20H10Z" fill="#67D7C9"/></svg>
  <div class="abs foot-item" style="left:962px;top:4497px">Privacy Policy</div>
  <svg class="abs" style="left:923px;top:4557px" width="28" height="20" viewBox="0 0 28 20"><path d="M0 10L10 0H28V20H10Z" fill="#67D7C9"/></svg>
  <div class="abs foot-item" style="left:962px;top:4558px">Terms and Use</div>

  <div class="abs copyright">2022 Verdance Health. All rights reserved.</div>
</footer>

</body>
</html>
```